M25 Billboard Advert Required Please

I need an advert for a motorway Billboard on the M25 , the advert should show the following in big letters:
GUTTER CLEANING
TOMSDRAINWORKS.NET and a small logo off to the side (Our logo is attached)

The printer has requested the following (Important please) the advert has to be
pdf file / 300 dpi/landscape orientation / scaled to a minimum 25% advert size ( this particular site is 22ft x 10ft so 25% of this please). Please also make sure that the artwork is embedded and outlined correctly if this is incorrect it will affect the printing of the banner.
Updates

Need extra days to review

Target Market(s)

General Public

Industry/Entity Type

Gutter Cleaning

Requirements
Should not have
• No Change to our Logo

```html
<!DOCTYPE html>
<html lang="en">
<head>
<meta charset="utf-8">
<title>Tom's Drainworks – Gutter Cleaning Billboard</title>
<link rel="stylesheet" href="https://fonts.googleapis.com/css2?family=Archivo:wdth,wght@62..125,400;62..125,600;62..125,900&display=swap">
<style>
  :root {
    --page-bg: #e9e9e9;
    --board-bg: #fbfcfd;
    --gold: #d5ae0c;
    --band: #e2c03e;
    --ink: #0d0d0d;
    --red: #990000;
    --sign-light: #f0d23a;
    --sign-dark: #c9a512;
  }
  * { box-sizing: border-box; margin: 0; padding: 0; }
  html, body { width: 1168px; height: 1200px; overflow: hidden; }
  body {
    background: var(--page-bg);
    font-family: "Archivo", sans-serif;
    position: relative;
  }
  .billboard {
    position: absolute;
    left: 0; top: 320px;
    width: 1168px; height: 560px;
    background: var(--board-bg);
    overflow: hidden;
  }
  .bottom-band {
    position: absolute;
    left: 0; right: 0; bottom: 0;
    height: 120px;
    background: var(--band);
  }
  .gold-frame {
    position: absolute;
    left: 28px; top: 12px; right: 28px; bottom: 14px;
    border: 15px solid var(--gold);
  }
  .sign-photo {
    position: absolute;
    background: linear-gradient(160deg, var(--sign-light), var(--sign-dark));
    border-radius: 6px;
  }
  .sign-photo--right-a { left: 862px; top: 98px; width: 130px; height: 160px; transform: rotate(-35deg); }
  .sign-photo--right-b { left: 1010px; top: 62px; width: 118px; height: 210px; transform: rotate(-12deg); }
  .sign-photo--left { left: 0; top: 238px; width: 70px; height: 260px; }
  .brand {
    position: absolute;
    left: 150px; top: 48px;
  }
  .brand__row { display: flex; align-items: center; gap: 14px; }
  .brand__mark { width: 22px; height: 22px; background: var(--ink); }
  .brand__name {
    font-weight: 900;
    font-size: 44px;
    color: var(--ink);
    letter-spacing: -1px;
  }
  .brand__tagline {
    margin-top: 14px;
    font-size: 19px;
    font-weight: 600;
    color: #333;
    letter-spacing: 0.5px;
  }
  .headline {
    position: absolute;
    left: 112px; top: 172px;
    font-weight: 900;
    font-stretch: 125%;
    font-size: 124px;
    line-height: 102px;
    letter-spacing: -2px;
    color: var(--ink);
  }
  .headline__accent { color: var(--red); }
  .web-address {
    position: absolute;
    left: 116px; top: 470px;
    font-weight: 900;
    font-stretch: 125%;
    font-size: 50px;
    color: var(--ink);
    letter-spacing: -0.5px;
  }
</style>
</head>
<body>
  <section class="billboard" aria-label="Gutter cleaning billboard">
    <div class="bottom-band"></div>
    <div class="sign-photo sign-photo--left" role="img" aria-label="Yellow caution cleaning-in-progress floor sign, cropped at edge"></div>
    <div class="sign-photo sign-photo--right-a" role="img" aria-label="Yellow caution floor sign seen from the back"></div>
    <div class="sign-photo sign-photo--right-b" role="img" aria-label="Yellow caution cleaning-in-progress floor sign"></div>
    <div class="gold-frame"></div>

    <div class="brand">
      <div class="brand__row">
        <span class="brand__mark"></span>
        <span class="brand__name">Tom's Drainworks</span>
      </div>
      <p class="brand__tagline">Clean gutters protect your property</p>
    </div>

    <h1 class="headline">GUTTER<br><span class="headline__accent">CLEA</span>NING</h1>

    <p class="web-address">TOMSDRAINWORKS.NET</p>
  </section>
</body>
</html>
```